Hadley & Partners, LLC Business Card 2016

We need a new business card design for a very important trade show coming up.

We are a compliance Consulting Firm. Our clients are stock brokerage firms and investment advisers.

I would like our logo on both sides of the card.

Info in the front of the card shold include:

Logo
First & Last Name
Title
Office #
Cell #
Email
Company Address (42 W. Calloway St., Suite 300 Pasadena, CA 91417

Back of the card should include the logo and url: www.hadleypartnersgroup.com

Target Market(s)

Stock Brokerage Firms and Investment Advisers

Industry/Entity Type

Financial Service

Contact Information for Business Card

Marcus J. Pellew
President
42 W. Calloway St., Suite 300
Pasadena, CA 91417
O 626.555.0147 ext. 204
C 818.555.0193
Email: marcus@hadleypartnersgroup.com
www.hadleypartnersgroup.com

Requirements
Nice to have
• The back of the card could be black with the logo with the white letters.
• I do want the front of the card to at least have the color logo with the black "Hadley & Partners Lettering.

```html
<!DOCTYPE html>
<html lang="en">
<head>
<meta charset="utf-8">
<title>Hadley &amp; Partners — Business Card</title>
<link href="https://fonts.googleapis.com/css2?family=Marcellus+SC&display=swap" rel="stylesheet">
<style>
  :root {
    --backdrop: #e9e6e2;
    --card: #2a2a2b;
    --silver: #c9c9c9;
    --soft-white: #e4e4e4;
    --band: #8c8c8c;
    --ink: #111111;
    --accent-red: #c3161c;
    --rule: #9a9a9a;
  }
  * { margin: 0; padding: 0; box-sizing: border-box; }
  html, body {
    width: 1200px; height: 1000px; overflow: hidden;
    background: var(--backdrop);
    font-family: "Marcellus SC", "Times New Roman", serif;
  }
  .card {
    position: absolute; top: 30px; width: 515px; height: 855px;
    background: var(--card); border-radius: 24px; overflow: hidden;
    box-shadow: 0 6px 18px rgba(0,0,0,.25);
    text-align: center;
  }
  .card--back { left: 45px; }
  .card--front { left: 645px; }

  .brand {
    position: absolute; left: 0; right: 0;
    color: var(--silver); line-height: 1;
  }
  .brand__name { font-size: 56px; letter-spacing: 1px; }
  .card--back .brand { top: 330px; }

  .tagline {
    position: absolute; left: 0; right: 0; top: 604px;
    color: var(--soft-white); font-size: 23px; line-height: 29px; letter-spacing: 1px;
  }
  .rule {
    position: absolute; height: 1px; background: var(--rule);
  }
  .card--back .rule--left { left: 0; width: 132px; top: 617px; }
  .card--back .rule--right { right: 0; width: 125px; top: 617px; }

  .url {
    position: absolute; left: 0; right: 0; top: 788px;
    color: var(--soft-white); font-size: 16px; letter-spacing: 1.5px;
  }

  .band {
    position: absolute; left: 0; right: 0; top: 165px; height: 118px;
    background: var(--band);
    display: flex; align-items: center; justify-content: center;
  }
  .band .brand__name { color: var(--ink); font-size: 54px; }

  .person {
    position: absolute; left: 0; right: 0; top: 355px;
    color: var(--soft-white);
  }
  .person__name { font-size: 36px; line-height: 56px; letter-spacing: 3px; }
  .person__title { color: var(--accent-red); font-size: 23px; letter-spacing: 3px; margin-top: 2px; }

  .contact {
    position: absolute; left: 0; right: 0; top: 633px;
    color: var(--soft-white); font-size: 14.5px; letter-spacing: 1.3px; line-height: 19.5px;
    list-style: none;
  }
  .contact li + li.contact__mobile { margin-top: 4px; }
  .contact li.contact__email { margin-top: 3px; }
  .card--front .rule--left { left: 0; width: 75px; top: 682px; }
  .card--front .rule--right { right: 0; width: 78px; top: 682px; }
</style>
</head>
<body>
  <section class="card card--back" aria-label="Card back">
    <div class="brand"><div class="brand__name">Hadley &amp; Partners</div></div>
    <p class="tagline">Innovative<br>Professional<br>Leaders</p>
    <span class="rule rule--left"></span>
    <span class="rule rule--right"></span>
    <p class="url">www.hadleypartnersgroup.com</p>
  </section>

  <section class="card card--front" aria-label="Card front">
    <div class="band"><div class="brand__name">Hadley &amp; Partners</div></div>
    <div class="person">
      <h1 class="person__name">Marcus J.<br>Pellew</h1>
      <p class="person__title">President</p>
    </div>
    <ul class="contact">
      <li>42 W. Calloway St., Suite 300</li>
      <li>Pasadena, CA 91417</li>
      <li>office: 626.555.0147 ext. 204</li>
      <li class="contact__mobile">mobile: 818.555.0193</li>
      <li class="contact__email">marcus@hadleypartnersgroup.com</li>
    </ul>
    <span class="rule rule--left"></span>
    <span class="rule rule--right"></span>
  </section>
</body>
</html>
```